Designing a brochures for an educational counseling service provider

We would like a 4 sided design on a 11x8.5 paper, half folded. I have including a sample design we did to give you an idea of what we envision but we welcome creativity to make beautiful looking flyers. Text for the flier is included as well as our logo.
- The most important thing is capturing our audience/market. We will be handing these flies to schools, organizations and individual clients.

www.vormtaleducationalconsultants.com

Target Market(s)

We are targeting international students wanting to study in the U.S and Canada.

Industry/Entity Type

Education

Requirements
Must have
• - Clean and clear
• - Our logo should visible and well placed.
• - Could you the pictures of students, libraries and school buildings or you could use the pictures we already have.
Nice to have
• We would like this to match business cards.

```html
<!DOCTYPE html>
<html lang="en">
<head>
<meta charset="utf-8">
<title>Vormtal Educational Consultants – Brochure Spread</title>
<link href="https://fonts.googleapis.com/css2?family=Questrial&display=swap" rel="stylesheet">
<style>
  :root{
    --navy:#1b2433;
    --orange:#e0762a;
    --white:#ffffff;
    --ink:#2a2f3a;
    --bg:#dfe7ea;
  }
  *{box-sizing:border-box;margin:0;padding:0}
  html,body{width:1200px;height:789px;overflow:hidden;background:var(--bg)}
  body{font-family:"Questrial",sans-serif;position:relative}
  .spread{position:absolute;left:121px;top:24px;width:958px;height:740px;display:flex;box-shadow:0 4px 14px rgba(0,0,0,.15)}
  .page{position:relative;width:479px;height:740px;overflow:hidden}

  /* back cover */
  .back{background:var(--navy)}
  .back .hero-photo{position:absolute;left:0;top:0;width:479px;height:450px;
    background:linear-gradient(160deg,#d8e2c8 0%,#b7c79a 30%,#efe9dc 55%,#c99a72 80%,#8a6a52 100%)}
  .back .bands{position:absolute;left:0;top:0}
  .back .portrait{position:absolute;left:80px;top:330px;width:160px;height:160px;border-radius:50%;
    border:6px solid var(--white);background:radial-gradient(circle at 45% 45%,#8a5a3c,#4a2e22 70%,#2b1d18)}
  .contact{position:absolute;left:40px;top:512px;right:30px;color:var(--white)}
  .contact-title{font-size:26px;line-height:1.2;letter-spacing:.5px;padding-bottom:6px;border-bottom:1px solid rgba(255,255,255,.6);width:230px}
  .contact-role{margin-top:8px;color:var(--orange);font-size:13px;line-height:1.25}
  .contact-list{list-style:none;margin-top:10px;font-size:11.5px;line-height:1.3}
  .contact-list li{display:flex;align-items:flex-start;gap:10px;margin-bottom:4px}
  .contact-list svg{flex:none;margin-top:1px}
  .social{position:absolute;right:34px;top:520px;display:flex;gap:6px}
  .social span{width:20px;height:20px;border-radius:4px;background:var(--orange)}

  /* front cover */
  .front{background:var(--white)}
  .brand{position:absolute;left:0;right:0;top:48px;display:flex;justify-content:center;align-items:center;gap:12px}
  .brand-mark{width:26px;height:26px;border-radius:50%;background:var(--navy)}
  .brand-name{font-size:34px;letter-spacing:3px;color:var(--navy)}
  .headline{position:absolute;left:30px;right:30px;top:128px;text-align:center;font-size:14px;line-height:1.35;color:var(--ink);text-transform:uppercase;letter-spacing:.3px}
  .headline em{font-style:normal;color:var(--orange)}
  .front .group-photo{position:absolute;left:0;top:196px;width:479px;height:300px;
    background:linear-gradient(180deg,#e9ecef 0%,#c9d2cf 30%,#a9b88c 55%,#6f8f4a 80%,#577a3a 100%)}
  .front .bands{position:absolute;left:0;top:0}
  .services{position:absolute;left:0;right:0;top:440px}
  .service-icon{position:absolute;width:76px;height:76px;border-radius:50%;background:var(--navy);border:4px solid var(--white);display:flex;align-items:center;justify-content:center}
  .service-label{position:absolute;width:100px;text-align:center;font-size:13px;line-height:1.15;color:var(--ink);text-transform:uppercase}
  .label-divider{position:absolute;width:1px;height:40px;background:#9aa0a8}
  .site{position:absolute;left:0;right:24px;top:676px;text-align:right;font-size:13px;color:var(--orange)}
  .site-rule{position:absolute;left:40px;right:24px;top:670px;height:1px;background:#b9bdc3}
</style>
</head>
<body>
<main class="spread">
  <section class="page back">
    <div class="hero-photo" role="img" aria-label="Photo of smiling teenage girls in sports jerseys holding a soccer ball in front of a goal net"></div>
    <svg class="bands" width="479" height="740" viewBox="0 0 479 740" aria-hidden="true">
      <path d="M0 270 C120 360 300 410 479 420 L479 740 L0 740 Z" fill="var(--white)"/>
      <path d="M0 282 C120 372 300 422 479 432 L479 740 L0 740 Z" fill="var(--orange)"/>
      <path d="M0 294 C120 384 300 434 479 444 L479 740 L0 740 Z" fill="var(--white)"/>
      <path d="M0 302 C120 392 300 442 479 452 L479 740 L0 740 Z" fill="var(--navy)"/>
    </svg>
    <div class="portrait" role="img" aria-label="Circular photo of two smiling young women"></div>
    <div class="social" aria-hidden="true"><span></span><span></span></div>
    <div class="contact">
      <h2 class="contact-title">Contact us:</h2>
      <p class="contact-role">Executive Director &amp; Independent<br>Educational Consultant<br>Vormtal International Educational Consultants, LLC</p>
      <ul class="contact-list">
        <li><svg width="13" height="13" viewBox="0 0 16 16"><path d="M8 1a5 5 0 0 0-5 5c0 4 5 9 5 9s5-5 5-9a5 5 0 0 0-5-5zm0 7a2 2 0 1 1 0-4 2 2 0 0 1 0 4z" fill="var(--orange)"/></svg><span>1840 Ridgeway Rd<br>Suite 310, Maplecrest, TX 75012</span></li>
        <li><svg width="13" height="13" viewBox="0 0 16 16"><path d="M4 1l3 3-2 2c1 2 3 4 5 5l2-2 3 3-2 3C7 15 1 9 1 3z" fill="var(--orange)"/></svg><span>555-210-4836</span></li>
        <li><svg width="13" height="13" viewBox="0 0 16 16"><rect x="1" y="3" width="14" height="10" rx="1" fill="var(--orange)"/><path d="M1 4l7 5 7-5" stroke="var(--navy)" fill="none"/></svg><span>contact@vormtaleducationalconsultants.com</span></li>
        <li><svg width="13" height="13" viewBox="0 0 16 16"><circle cx="8" cy="8" r="6.5" fill="none" stroke="var(--orange)" stroke-width="1.5"/><path d="M1.5 8h13M8 1.5c-3 3-3 10 0 13M8 1.5c3 3 3 10 0 13" stroke="var(--orange)" fill="none"/></svg><span>vormtaleducationalconsultants.com</span></li>
      </ul>
    </div>
  </section>

  <section class="page front">
    <div class="brand"><span class="brand-mark"></span><span class="brand-name">VORMTAL</span></div>
    <p class="headline">A full-service international educational consulting group serving <em>students and families</em> across the globe.</p>
    <div class="group-photo" role="img" aria-label="Photo of a diverse group of university students sitting together on a bench in a park with a city skyline behind"></div>
    <svg class="bands" width="479" height="740" viewBox="0 0 479 740" aria-hidden="true">
      <path d="M0 500 C160 520 330 470 479 420 L479 740 L0 740 Z" fill="var(--white)"/>
      <path d="M0 490 C160 508 330 458 479 404 L479 416 C330 470 160 520 0 502 Z" fill="var(--orange)"/>
      <path d="M0 508 C160 526 330 476 479 426 L479 432 C330 482 160 532 0 514 Z" fill="var(--orange)"/>
    </svg>
    <div class="services">
      <div class="service-icon" style="left:38px;top:64px"><svg width="38" height="34" viewBox="0 0 38 34"><path d="M19 2L2 10h34z" fill="#fff"/><rect x="4" y="12" width="30" height="3" fill="#fff"/><rect x="7" y="17" width="4" height="11" fill="#fff"/><rect x="14" y="17" width="4" height="11" fill="#fff"/><rect x="21" y="17" width="4" height="11" fill="#fff"/><rect x="28" y="17" width="4" height="11" fill="#fff"/><rect x="3" y="29" width="32" height="3" fill="#fff"/></svg></div>
      <div class="service-icon" style="left:148px;top:42px"><svg width="32" height="34" viewBox="0 0 32 34"><rect x="3" y="2" width="22" height="29" rx="2" fill="none" stroke="#fff" stroke-width="2.5"/><path d="M8 10h12M8 15h12M8 20h8" stroke="#fff" stroke-width="2"/><path d="M29 14l-9 12-2 4 4-2 9-12z" fill="#fff"/></svg></div>
      <div class="service-icon" style="left:258px;top:14px"><svg width="42" height="30" viewBox="0 0 42 30"><circle cx="21" cy="8" r="6" fill="#fff"/><path d="M10 29c0-9 5-13 11-13s11 4 11 13z" fill="#fff"/><circle cx="9" cy="10" r="4.5" fill="#fff"/><path d="M1 27c0-7 4-10 8-10 2 0 3 .5 4 1-2 2-3 5-3 9z" fill="#fff"/><circle cx="33" cy="10" r="4.5" fill="#fff"/><path d="M41 27c0-7-4-10-8-10-2 0-3 .5-4 1 2 2 3 5 3 9z" fill="#fff"/></svg></div>
      <div class="service-icon" style="left:368px;top:-14px"><svg width="42" height="30" viewBox="0 0 42 30"><path d="M21 2L1 11l20 9 20-9z" fill="#fff"/><path d="M9 15v8c3 3 7 4 12 4s9-1 12-4v-8l-12 5z" fill="#fff"/><path d="M37 13v10" stroke="#fff" stroke-width="2"/></svg></div>

      <p class="service-label" style="left:26px;top:160px">Boarding<br>Schools</p>
      <span class="label-divider" style="left:130px;top:148px"></span>
      <p class="service-label" style="left:136px;top:140px">College<br>Admission</p>
      <span class="label-divider" style="left:240px;top:126px"></span>
      <p class="service-label" style="left:246px;top:118px">Transfer<br>Students</p>
      <span class="label-divider" style="left:350px;top:102px"></span>
      <p class="service-label" style="left:356px;top:96px">Graduate<br>Students</p>
    </div>
    <span class="site-rule"></span>
    <p class="site">www.vormtaleducationalconsultants.com</p>
  </section>
</main>
</body>
</html>
```